Tech business card design

We need an amazing business card design for our new business 'Brakka' a marketing tech startup based in Sydney, Australia. We provide an online marketplace for businesses to search and buy advertising media, connect with service providers and learn more about marketing. We wish to communicate 'cool tech', reliability and professionalism and design based around our logo.

Target Market(s)

Business Owners

Contact Information for Business Card

Name
Position
Email Address
Website
Phone Number

Font styles to use
Other font styles liked:
• Avenir & Avenir Next

Colors

Designer to choose colors to be used in the design.

```html
<!DOCTYPE html>
<html lang="en">
<head>
<meta charset="UTF-8">
<title>Brakka Business Card</title>
<link href="https://fonts.googleapis.com/css2?family=Nunito+Sans:wght@300;400;700;800&display=swap" rel="stylesheet">
<style>
  :root {
    --backdrop: #2b2d31;
    --card-navy: #1b1a5e;
    --card-navy-deep: #141347;
    --ink-light: #f2f3f8;
    --ink-muted: #b9bbd3;
    --rule: #d9dbea;
  }
  * { box-sizing: border-box; margin: 0; padding: 0; }
  html, body {
    width: 1200px; height: 900px; overflow: hidden;
    background: var(--backdrop);
    font-family: "Nunito Sans", "Avenir Next", Avenir, sans-serif;
  }
  .sheet {
    width: 1200px; height: 900px;
    display: flex; flex-direction: column;
    align-items: center; justify-content: center; gap: 60px;
  }
  .card {
    position: relative;
    width: 600px; height: 343px;
    border-radius: 26px;
    background: linear-gradient(150deg, var(--card-navy) 0%, var(--card-navy-deep) 100%);
    box-shadow: 0 4px 0 #12113d, 0 8px 0 #0f0e34, 0 22px 40px rgba(0,0,0,.45);
    color: var(--ink-light);
  }
  .brand-name {
    font-weight: 800;
    color: var(--ink-light);
    letter-spacing: -1px;
    line-height: 1;
  }
  /* Back side: centred wordmark */
  .card-back { display: flex; align-items: center; justify-content: center; }
  .card-back .brand-name { font-size: 96px; }

  /* Front side: wordmark, divider, contact block */
  .card-front { display: flex; align-items: center; padding: 0 40px 0 52px; }
  .card-front .brand-name { font-size: 64px; width: 215px; }
  .divider {
    width: 1.5px; height: 190px;
    background: var(--rule);
    margin: 0 26px 0 14px;
  }
  .contact { display: flex; flex-direction: column; }
  .person-name { font-weight: 700; font-size: 24px; letter-spacing: 2px; }
  .person-role { font-weight: 300; font-size: 13px; color: var(--ink-muted); margin: 4px 0 26px; letter-spacing: .5px; }
  .contact-line {
    display: flex; align-items: center; gap: 10px;
    font-weight: 400; font-size: 15px; letter-spacing: 2.4px;
    color: var(--ink-light); margin-bottom: 6px;
  }
  .contact-line svg { width: 11px; height: 11px; flex: none; }
</style>
</head>
<body>
  <main class="sheet">
    <section class="card card-back">
      <span class="brand-name">brakka</span>
    </section>

    <section class="card card-front">
      <span class="brand-name">brakka</span>
      <div class="divider"></div>
      <div class="contact">
        <div class="person-name">Marcus Reid</div>
        <div class="person-role">Founder / Director</div>
        <div class="contact-line">
          <svg viewBox="0 0 12 12" aria-hidden="true"><rect x="3" y="0.5" width="6" height="11" rx="1.2" fill="none" stroke="#f2f3f8" stroke-width="1.2"/><circle cx="6" cy="9.5" r="0.8" fill="#f2f3f8"/></svg>
          <span>+61 (0)412 587 209</span>
        </div>
        <div class="contact-line">
          <svg viewBox="0 0 12 12" aria-hidden="true"><rect x="0.6" y="2" width="10.8" height="8" rx="1" fill="#f2f3f8"/><path d="M1 2.5 L6 6.5 L11 2.5" fill="none" stroke="#1b1a5e" stroke-width="1.1"/></svg>
          <span>marcus@brakkamedia.com.au</span>
        </div>
        <div class="contact-line">
          <svg viewBox="0 0 12 12" aria-hidden="true"><circle cx="6" cy="6" r="5.3" fill="none" stroke="#f2f3f8" stroke-width="1.1"/><ellipse cx="6" cy="6" rx="2.3" ry="5.3" fill="none" stroke="#f2f3f8" stroke-width="0.9"/><line x1="0.8" y1="6" x2="11.2" y2="6" stroke="#f2f3f8" stroke-width="0.9"/></svg>
          <span>www.brakkamedia.com.au</span>
        </div>
      </div>
    </section>
  </main>
</body>
</html>
```